Food Menu Design for Japanese Restaurant

Design a food menu for a high-end Japanese food restaurant. See attached detailed requirements file and menu items.

Industry/Entity Type

Restaurant

Colors

Designer to choose colors to be used in the design.

Requirements
Must have
• All menu items, descriptions, prices, add-ons, as provided in requirements file, all shown on designed menu and formatted.

```html
<!DOCTYPE html>
<html lang="en">
<head>
<meta charset="utf-8">
<title>Sushi a la Carte – Namiko</title>
<link href="https://fonts.googleapis.com/css2?family=Lato:ital,wght@0,400;0,700;1,400&display=swap" rel="stylesheet">
<style>
  :root {
    --navy: #1d3452;
    --bloom: rgba(90, 111, 168, 0.35);
    --bloom-mid: rgba(90, 111, 168, 0.18);
    --bloom-fade: rgba(29, 52, 82, 0);
    --text: #ffffff;
    --text-soft: #e6ebf3;
    --rule: rgba(255, 255, 255, 0.38);
  }
  * { margin: 0; padding: 0; box-sizing: border-box; }
  html, body {
    width: 1200px;
    height: 2400px;
    overflow: hidden;
    background: var(--navy);
  }
  .menu {
    position: relative;
    width: 1200px;
    height: 2400px;
    background: var(--navy);
    font-family: "Lato", sans-serif;
    color: var(--text);
    overflow: hidden;
  }
  .bloom {
    position: absolute;
    border-radius: 50%;
    background: radial-gradient(circle, var(--bloom) 0%, var(--bloom-mid) 45%, var(--bloom-fade) 72%);
  }
  .bloom--top-right { width: 420px; height: 420px; right: -120px; top: -110px; }
  .bloom--left { width: 300px; height: 300px; left: -150px; top: 640px; }
  .bloom--right { width: 260px; height: 260px; right: -130px; top: 1300px; }
  .bloom--bottom-left { width: 380px; height: 380px; left: -120px; top: 1720px; }
  .bloom--bottom-corner { width: 340px; height: 340px; left: 60px; top: 2150px; }

  .menu__title {
    position: absolute;
    left: 142px;
    top: 120px;
    font-weight: 400;
    font-size: 94px;
    line-height: 1.1;
    letter-spacing: 1px;
    color: var(--text);
  }

  .menu-table {
    position: absolute;
    left: 155px;
    top: 272px;
    width: 927px;
    border-collapse: collapse;
    table-layout: fixed;
  }
  .menu-table th, .menu-table td { padding: 0; }
  .menu-table col.col-item { width: 500px; }
  .menu-table col.col-nigiri { width: 144px; }
  .menu-table col.col-sashimi { width: 178px; }
  .menu-table col.col-end { width: 105px; }

  .menu-table thead th {
    height: 134px;
    vertical-align: top;
    text-align: center;
    font-weight: 700;
    font-size: 22px;
    line-height: 1.2;
    color: var(--text);
  }
  .portion {
    display: block;
    font-weight: 400;
    font-style: italic;
    font-size: 19px;
    color: var(--text-soft);
  }

  .menu-table tbody td {
    height: 54px;
    font-size: 21px;
    font-weight: 400;
    color: var(--text-soft);
    border-bottom: 2px dotted var(--rule);
    vertical-align: middle;
    white-space: nowrap;
  }
  .menu-table tbody tr:last-child td { border-bottom: none; }
  .menu-table .price { text-align: center; }

  .brand-name {
    position: absolute;
    right: 118px;
    top: 2210px;
    font-weight: 400;
    font-size: 48px;
    letter-spacing: 0;
    color: var(--text);
  }
</style>
</head>
<body>
<div class="menu">
  <div class="bloom bloom--top-right" role="img" aria-label="Faint line-drawn chrysanthemum flowers"></div>
  <div class="bloom bloom--left" role="img" aria-label="Faint line-drawn chrysanthemum flower"></div>
  <div class="bloom bloom--right" role="img" aria-label="Faint line-drawn chrysanthemum flower"></div>
  <div class="bloom bloom--bottom-left" role="img" aria-label="Faint line-drawn chrysanthemum flowers"></div>
  <div class="bloom bloom--bottom-corner" role="img" aria-label="Faint line-drawn chrysanthemum flowers"></div>

  <h1 class="menu__title">SUSHI A LA CARTE</h1>

  <table class="menu-table">
    <colgroup>
      <col class="col-item"><col class="col-nigiri"><col class="col-sashimi"><col class="col-end">
    </colgroup>
    <thead>
      <tr>
        <th></th>
        <th>Nigiri<span class="portion">2 pieces<br>per order</span></th>
        <th>Sashimi<span class="portion">3 pieces<br>per order</span></th>
        <th></th>
      </tr>
    </thead>
    <tbody>
      <tr><td>Surf Clam (Hokkigai)</td><td class="price">4</td><td class="price">6</td><td></td></tr>
      <tr><td>Egg Omelet (Tamago)</td><td class="price">4</td><td class="price">6</td><td></td></tr>
      <tr><td>Fresh Water Eel (Unagi)</td><td class="price">6</td><td class="price">8</td><td></td></tr>
      <tr><td>Flying Fish Roe (Tobiko)</td><td class="price">5</td><td class="price">7</td><td></td></tr>
      <tr><td>Fried Tofu Pocket (Inari)</td><td class="price">4</td><td class="price">-</td><td></td></tr>
      <tr><td>Imitation Crab (Kani)</td><td class="price">4</td><td class="price">6</td><td></td></tr>
      <tr><td>Mackerel (Saba)</td><td class="price">5</td><td class="price">7</td><td></td></tr>
      <tr><td>Horse Mackerel (Aji)</td><td class="price">7</td><td class="price">9</td><td></td></tr>
      <tr><td>Red Snapper (Izumidai)</td><td class="price">5</td><td class="price">7</td><td></td></tr>
      <tr><td>Salmon (Sake)</td><td class="price">5.5</td><td class="price">7.5</td><td></td></tr>
      <tr><td>Spicy Salmon</td><td class="price">7</td><td class="price">9</td><td></td></tr>
      <tr><td>Fatty Salmon</td><td class="price">7</td><td class="price">9</td><td></td></tr>
      <tr><td>Salmon Roe (Ikura)</td><td class="price">5.5</td><td class="price">7.5</td><td></td></tr>
      <tr><td>Smoked Salmon</td><td class="price">6</td><td class="price">8</td><td></td></tr>
      <tr><td>Scallop (Hotategai)</td><td class="price">6</td><td class="price">8</td><td></td></tr>
      <tr><td>Live Scallop</td><td class="price">-</td><td class="price">MP</td><td></td></tr>
      <tr><td>Shiitake Mushroom</td><td class="price">4</td><td class="price">6</td><td></td></tr>
      <tr><td>Shrimp (Ebi)</td><td class="price">5</td><td class="price">7</td><td></td></tr>
      <tr><td>Sweet Shrimp (Ama Ebi)</td><td class="price">9</td><td class="price">13</td><td></td></tr>
      <tr><td>Smelt Roe (Masago)</td><td class="price">4</td><td class="price">6</td><td></td></tr>
      <tr><td>Squid (Ika)</td><td class="price">5</td><td class="price">7</td><td></td></tr>
      <tr><td>Tuna (Maguro)</td><td class="price">6</td><td class="price">8</td><td></td></tr>
      <tr><td>Spicy Tuna</td><td class="price">7</td><td class="price">9</td><td></td></tr>
      <tr><td>Albacore (Bincho Maguro)</td><td class="price">6</td><td class="price">8</td><td></td></tr>
      <tr><td>Fatty Tuna (Toro)</td><td class="price">MP</td><td class="price">MP</td><td></td></tr>
      <tr><td>Seared Tuna</td><td class="price">7</td><td class="price">9</td><td></td></tr>
      <tr><td>Octopus (Tako)</td><td class="price">5</td><td class="price">7</td><td></td></tr>
      <tr><td>Sea Urchin (Uni)</td><td class="price">MP</td><td class="price">MP</td><td></td></tr>
      <tr><td>White Tuna (Shiro Maguro)</td><td class="price">6</td><td class="price">8</td><td></td></tr>
      <tr><td>Yellowtail (Hamachi)</td><td class="price">6</td><td class="price">8</td><td></td></tr>
      <tr><td>Sea Water Eel (Anago)</td><td class="price">7</td><td class="price">9</td><td></td></tr>
    </tbody>
  </table>

  <div class="brand-name">Namiko</div>
</div>
</body>
</html>
```